Pretty up existing catalogue

Catalog available - should simply be made new / fresh - ideally in corel draw? Please use page 14 as a sample design! Many thanks. Otherwise you can let off steam completely in terms of design. Thanks

Target Market(s)

customers worldwide

Industry/Entity Type

Bau

Font styles to use
Serif
Sans Serif

Requirements
Must have
• Logo must remain the same, modern look
Nice to have
• fresh modern look
Should not have
• extreme colors, log change

```html
<!DOCTYPE html>
<html lang="de">
<head>
<meta charset="utf-8">
<title>Haltenadeln</title>
<link href="https://fonts.googleapis.com/css2?family=Outfit:wght@300;400;600&display=swap" rel="stylesheet">
<style>
  :root {
    --backdrop: #e4e5ea;
    --sheet-dark: #2b2b2d;
    --brand-yellow: #d8c419;
    --band-yellow: #e6d31a;
    --card-top: #ffffff;
    --card-bottom: #ececec;
    --ink: #1f1f1f;
    --ink-soft: #555556;
  }
  * { margin: 0; padding: 0; box-sizing: border-box; }
  html, body { width: 1200px; height: 800px; overflow: hidden; }
  body {
    background: var(--backdrop);
    font-family: "Outfit", sans-serif;
    color: var(--ink);
    position: relative;
  }
  .sheet {
    position: absolute;
    left: 321px; top: 8px;
    width: 558px; height: 784px;
    background: var(--sheet-dark);
    overflow: hidden;
  }
  .sheet-header {
    position: absolute; left: 0; top: 0;
    width: 100%; height: 134px;
    background: var(--brand-yellow);
    border-bottom-right-radius: 110px 120px;
  }
  .sheet-title {
    position: absolute; left: 45px; top: 24px;
    font-size: 34px; font-weight: 600; letter-spacing: -0.5px;
    color: var(--ink);
  }
  .sheet-subtitle {
    position: absolute; left: 45px; top: 64px;
    font-size: 19px; font-weight: 300; line-height: 1.1;
    color: var(--ink);
  }
  .header-visual {
    position: absolute; left: 372px; top: 14px;
    width: 152px; height: 108px;
    border-radius: 20px;
    background: linear-gradient(135deg, #c9cbcc, #8d9092);
  }
  .catalog-grid {
    position: absolute; left: 47px; top: 157px;
    display: grid;
    grid-template-columns: 215px 215px;
    grid-auto-rows: 138px;
    column-gap: 34px; row-gap: 13px;
  }
  .product-card {
    position: relative;
    border-radius: 9px;
    overflow: hidden;
    background: linear-gradient(180deg, var(--card-top), var(--card-bottom));
  }
  .card-band {
    height: 29px;
    background: var(--band-yellow);
    padding: 5px 0 0 17px;
    font-size: 16.5px; font-weight: 300;
    white-space: nowrap;
  }
  .card-band strong { font-weight: 600; }
  .card-body {
    padding: 9px 0 0 17px;
    font-size: 11.4px; line-height: 1.15;
  }
  .card-body .label { color: var(--ink); font-weight: 400; margin-top: 3px; }
  .card-body .label:first-child { margin-top: 0; }
  .card-body .value { color: var(--ink-soft); font-weight: 300; margin-top: 3px; }
  .product-visual {
    position: absolute; right: 5px; top: 6px;
    width: 40px; height: 76px;
    border-radius: 8px 8px 4px 4px;
  }
  .visual-blue { background: linear-gradient(180deg, #2b3fb0, #1b2a86); }
  .visual-red { background: linear-gradient(180deg, #e0363a, #b51d22); }
  .visual-green { background: linear-gradient(180deg, #1f6e25, #124a17); }
  .visual-black { background: linear-gradient(180deg, #3a3a3c, #1a1a1c); }
  .visual-navy { background: linear-gradient(180deg, #2e3488, #1f2466); }
  .visual-orange { background: linear-gradient(180deg, #f0683a, #d44e22); }
  .visual-lime { background: linear-gradient(180deg, #23b342, #128a2c); }
  .visual-tool { top: 4px; height: 126px; width: 40px; right: 12px; background: linear-gradient(180deg, #9a9ca0, #4a4b4e); }
</style>
</head>
<body>
  <main class="sheet">
    <header class="sheet-header">
      <h1 class="sheet-title">Haltenadeln</h1>
      <p class="sheet-subtitle">Zur Befestigung von Kestler Schienen,<br>Folien und Rohrbögen auf Isolation</p>
      <div class="header-visual" role="img" aria-label="Graues T-Rohrverbindungsstück"></div>
    </header>

    <section class="catalog-grid">
      <article class="product-card">
        <div class="card-band">Artikel Nr. <strong>4120</strong></div>
        <div class="product-visual visual-blue" role="img" aria-label="Blaue Haltenadel"></div>
        <div class="card-body">
          <p class="label">Länge:</p>
          <p class="value">39 mm Für Rohre mit<br>einem 0 bis 20 mm</p>
          <p class="label">Per Hand zu setzen Verpackung:</p>
          <p class="value">500 Stück/Beutel und 5.000<br>Stück/Karton</p>
        </div>
      </article>
      <article class="product-card">
        <div class="card-band">Artikel Nr. <strong>4130</strong></div>
        <div class="product-visual visual-red" role="img" aria-label="Rote Haltenadel"></div>
        <div class="card-body">
          <p class="label">Länge:</p>
          <p class="value">46 mm Für Rohre mit<br>einem Ø bis 20 mm</p>
          <p class="label">Per Hand zu setzen Verpackung:</p>
          <p class="value">500 Stück/Beutel und 5.000<br>Stück/Karton</p>
        </div>
      </article>
      <article class="product-card">
        <div class="card-band">Artikel Nr. <strong>4140</strong></div>
        <div class="product-visual visual-green" role="img" aria-label="Grüne Haltenadel"></div>
        <div class="card-body">
          <p class="label">Länge:</p>
          <p class="value">61 mm Für Rohre mit<br>einem 0 bis 20 mm</p>
          <p class="label">Per Hand zu setzen Verpackung:</p>
          <p class="value">500 Stück/Beutel und 5.000<br>Stück/Karton</p>
        </div>
      </article>
      <article class="product-card">
        <div class="card-band">Artikel Nr. <strong>5235</strong></div>
        <div class="product-visual visual-black" role="img" aria-label="Schwarze Haltenadel"></div>
        <div class="card-body">
          <p class="label">Länge:</p>
          <p class="value">52 mm Für Rohre mit<br>einem 0 bis 26 mm</p>
          <p class="label">Per Hand zu setzen Verpackung:</p>
          <p class="value">100 Stück/Beutel und 1.000<br>Stück/Karton</p>
        </div>
      </article>
      <article class="product-card">
        <div class="card-band">Artikel Nr. <strong>KSN40</strong></div>
        <div class="product-visual visual-navy" role="img" aria-label="Dunkelblaue Haltenadel"></div>
        <div class="card-body">
          <p class="label">Länge:</p>
          <p class="value">39 mm Für Rohre mit<br>einem Ø bis 20 mm</p>
          <p class="label">Mit KestPin zu setzen Verpackung:</p>
          <p class="value">250 Stück/Karton und Magaziniert<br>á 25 Stück</p>
        </div>
      </article>
      <article class="product-card">
        <div class="card-band">Artikel Nr. <strong>KSN50</strong></div>
        <div class="product-visual visual-orange" role="img" aria-label="Orange Haltenadel"></div>
        <div class="card-body">
          <p class="label">Länge:</p>
          <p class="value">47 mm Für Rohre mit<br>einem Ø bis 20 mm</p>
          <p class="label">Mit KestPin zu setzen Verpackung:</p>
          <p class="value">250 Stück/Karton und Magaziniert<br>á 25 Stück</p>
        </div>
      </article>
      <article class="product-card">
        <div class="card-band">Artikel Nr. <strong>KSN60</strong></div>
        <div class="product-visual visual-lime" role="img" aria-label="Hellgrüne Haltenadel"></div>
        <div class="card-body">
          <p class="label">Länge:</p>
          <p class="value">62 mm Für Rohre mit<br>einem 0 bis 20 mm</p>
          <p class="label">Mit KestPin zu setzen Verpackung:</p>
          <p class="value">250 Stück/Karton und Magaziniert<br>á 25 Stück</p>
        </div>
      </article>
      <article class="product-card">
        <div class="card-band">Artikel Nr. <strong>KSG</strong></div>
        <div class="product-visual visual-tool" role="img" aria-label="Setzgerät für Haltenadeln"></div>
        <div class="card-body">
          <p class="label">Setzgerät:</p>
          <p class="value">für Haltenadeln KSN40,<br>KSN50 und KSN60</p>
          <p class="label">Verpackung:</p>
          <p class="value">1 Stück/Karton</p>
        </div>
      </article>
    </section>
  </main>
</body>
</html>
```